Stonebrook 720 Real Estate Investment Company

We need a business card designed for a real estate investment company named Stonebrook 720. We want to use red#f04a50, orange #f37122 and yellow #fbee3e as the color scheme. The logo colors will need to be modified from the current blue palette. I've attach VitaPathway logo example that captures the color scheme we're going for for Stonebrook 720. Looking for clean Sans Serif fonts.
Contact Information for Business Card
Daniel Furlow
Managing Partner
48317 Whitfield Lane, Suite 510
Tampa, FL 33718
813-555-4870 Mobile
dfurlow@stonebrook720.example
www.stonebrook720.example
Requirements
Must have
- Looking for creative responses.
Nice to have
- Must hit color palette... orange, red, yellow

```html
<!DOCTYPE html>
<html lang="en">
<head>
<meta charset="utf-8">
<title>Stonebrook 720 – Business Card</title>
<link href="https://fonts.googleapis.com/css2?family=Oswald:wght@600&family=Lato:wght@400&display=swap" rel="stylesheet">
<style>
  :root {
    --backdrop: #1b1b1b;
    --card: #0c0c0c;
    --card-edge: #232323;
    --yellow: #fbee3e;
    --orange: #f37122;
    --red: #f04a50;
    --silver: #9a9a9a;
    --ink-light: #f2f2f2;
  }
  * { margin: 0; padding: 0; box-sizing: border-box; }
  html, body {
    width: 1200px;
    height: 900px;
    overflow: hidden;
    background: var(--backdrop);
  }
  .canvas {
    position: relative;
    width: 1200px;
    height: 900px;
  }
  .card {
    position: absolute;
    width: 580px;
    height: 330px;
    background: var(--card);
    border: 1px solid var(--card-edge);
    border-radius: 22px;
    box-shadow: 0 14px 34px rgba(0,0,0,0.55);
    overflow: hidden;
  }
  .card--back { left: 110px; top: 70px; }
  .card--front { left: 510px; top: 500px; }

  .wordmark {
    position: absolute;
    display: flex;
    align-items: center;
    gap: 12px;
    font-family: "Oswald", sans-serif;
    font-weight: 600;
    letter-spacing: 0.5px;
    white-space: nowrap;
  }
  .wordmark__dot {
    width: 14px;
    height: 14px;
    border-radius: 50%;
  }
  .card--back .wordmark {
    left: 50%;
    top: 120px;
    transform: translateX(-50%);
    font-size: 36px;
    color: var(--silver);
  }
  .card--back .wordmark__dot { background: var(--silver); }
  .back-url {
    position: absolute;
    right: 70px;
    bottom: 60px;
    font-family: "Lato", sans-serif;
    font-size: 13px;
    color: var(--ink-light);
  }

  .card--front .wordmark {
    right: 90px;
    top: 70px;
    font-size: 34px;
    color: var(--yellow);
  }
  .card--front .wordmark__dot { background: var(--orange); }
  .divider {
    position: absolute;
    left: 0;
    right: 0;
    top: 150px;
    height: 2px;
    background: linear-gradient(90deg, var(--red) 0%, var(--orange) 50%, var(--yellow) 100%);
  }
  .person {
    position: absolute;
    left: 34px;
    top: 188px;
  }
  .person__name {
    font-family: "Oswald", sans-serif;
    font-weight: 600;
    font-size: 22px;
    line-height: 1.05;
    color: var(--yellow);
    text-transform: uppercase;
  }
  .person__title {
    font-family: "Lato", sans-serif;
    font-size: 17px;
    color: var(--ink-light);
    margin-bottom: 8px;
  }
  .contact-list { list-style: none; }
  .contact-list li {
    display: flex;
    align-items: center;
    gap: 10px;
    font-family: "Lato", sans-serif;
    font-size: 16px;
    line-height: 1.4;
    color: var(--ink-light);
  }
  .contact-list svg { width: 13px; height: 13px; flex: none; }
  .address {
    position: absolute;
    right: 36px;
    top: 172px;
    text-align: right;
    font-family: "Lato", sans-serif;
    font-size: 16px;
    line-height: 1.35;
    color: var(--ink-light);
  }
</style>
</head>
<body>
<main class="canvas">

  <section class="card card--back" aria-label="Card back">
    <div class="wordmark"><span>Stonebrook720</span><span class="wordmark__dot"></span></div>
    <p class="back-url">www.stonebrook720.example</p>
  </section>

  <section class="card card--front" aria-label="Card front">
    <div class="wordmark"><span>Stonebrook720</span><span class="wordmark__dot"></span></div>
    <div class="divider"></div>

    <div class="address">
      <p>48317 Whitfield Lane</p>
      <p>Suite 510 Tampa, FL 33718</p>
    </div>

    <div class="person">
      <p class="person__name">Daniel Furlow</p>
      <p class="person__title">Managing Partner</p>
      <ul class="contact-list">
        <li>
          <svg viewBox="0 0 16 16" aria-hidden="true"><path fill="#fbee3e" d="M3 1h3l1.5 4-2 1.2a8 8 0 0 0 4.3 4.3L11 8.5l4 1.5v3a2 2 0 0 1-2 2A12 12 0 0 1 1 3a2 2 0 0 1 2-2z"/></svg>
          <span>813-555-4870</span>
        </li>
        <li>
          <svg viewBox="0 0 16 16" aria-hidden="true"><rect x="1" y="3" width="14" height="10" fill="#fbee3e"/><path d="M1 3l7 6 7-6" fill="none" stroke="#0c0c0c" stroke-width="1.4"/></svg>
          <span>dfurlow@stonebrook720.example</span>
        </li>
        <li>
          <svg viewBox="0 0 16 16" aria-hidden="true"><circle cx="8" cy="8" r="7" fill="#fbee3e"/><path d="M1 8h14M8 1c-3 3.5-3 10.5 0 14M8 1c3 3.5 3 10.5 0 14" fill="none" stroke="#0c0c0c" stroke-width="1"/></svg>
          <span>www.stonebrook720.example</span>
        </li>
      </ul>
    </div>
  </section>

</main>
</body>
</html>
```